Küchenparty
Zielgruppe
Restaurant / Catering / Event Management
Zielgruppe ü 40
Aufgabenstellung
Klares, schlichtes und vorallem edles design
Den Valentinstag mal anders feiern?
mischen Sie sich mit Ihren Liebsten ins getrubel einer Großküche und erleben das exclusive Küchenflair!
Bunte Diskobeläuchtung, Musik und Gäste in der Küche....das gibt es nur zu ganz besonderen Anlässen!
Endlich haben Sie in unserer komplett neu renovierten Küche wieder die Möglichkeit unseren Köchen und Köchinnen über die Schulter zu schauen oder über Rezepte fachzusimpeln.
Wir freuen uns Sie zur ersten Küchenparty im Kaltwinds am See begrüßen zu dürfen!
Es erwartet Sie eine Veilzahl an speziell für Sie angerichteten Speisen.
Dazu genießen Sie Weine regionaler Weingüter und aus Italien.
Speisen und Getränke inclusive!
Preis pro Person 98€
Den Valentinstag mal anders beginnen;
mit höchstem Genuss aus Küche und Keller bei der Küchenparty im Kaltwds am See.
Schlagsworte:
Für Sie individuell angerichtete Speisen / die Küche in action für Sie!
Weine der Region
DJ und Party
Preis 98,00 €
inklusive:
Aperitif
Große Speisenvarietät (5 Gänge plus)
Regionale und italienische Weine
Logo muss vorhanden sein in rot odeer weiss
Kontaktdaten:
Kaltwinds am See
Lore-Fink platz 7
71032 Böblingen
Tel: 07031 58 317 6
Mail: event@kaltwinds-beispiel.de
www.kaltwinds-beispiel.de

```html
<!DOCTYPE html>
<html lang="de">
<head>
<meta charset="utf-8">
<title>Küchenparty – Kaltwinds am See</title>
<link href="https://fonts.googleapis.com/css2?family=Josefin+Sans:wght@100;300&family=Poiret+One&display=swap" rel="stylesheet">
<style>
  :root {
    --page: #ffffff;
    --card: #141516;
    --card-edge: #1b1c1e;
    --gold: #c9a24c;
    --gold-soft: rgba(201, 162, 76, 0.35);
    --white: #f4f4f4;
    --photo-dark: #3a2a1e;
    --photo-warm: #d79a3e;
  }
  * { margin: 0; padding: 0; box-sizing: border-box; }
  html, body { width: 1200px; height: 1200px; overflow: hidden; background: var(--page); }
  .canvas { position: relative; width: 1200px; height: 1200px; }

  .card {
    position: absolute;
    left: 10px;
    width: 1161px;
    height: 546px;
    background: radial-gradient(ellipse at center, var(--card-edge) 0%, var(--card) 70%);
    box-shadow: 4px 4px 6px rgba(0, 0, 0, 0.45);
    overflow: hidden;
  }
  .card--front { top: 5px; }
  .card--back { top: 579px; }

  .emblem-area {
    position: absolute;
    left: 267px; top: 112px;
    width: 712px; height: 305px;
    background: radial-gradient(ellipse at 50% 50%, var(--gold-soft) 0%, rgba(201,162,76,0.12) 45%, rgba(201,162,76,0) 72%);
  }
  .event-title {
    position: absolute;
    left: 0; right: 0; top: 213px;
    text-align: center;
    font-family: "Josefin Sans", sans-serif;
    font-weight: 100;
    font-size: 92px;
    line-height: 1;
    color: var(--white);
    letter-spacing: 1px;
  }

  .brand {
    position: absolute;
    font-family: "Poiret One", sans-serif;
    line-height: 1;
    color: var(--white);
    white-space: nowrap;
  }
  .card--front .brand { left: 56px; top: 486px; font-size: 24px; }
  .card--back .brand { left: 82px; top: 486px; font-size: 20px; }

  .headline {
    position: absolute;
    left: 103px; top: 62px;
    font-family: "Josefin Sans", sans-serif;
    font-weight: 300;
    font-size: 35px;
    line-height: 1;
    color: var(--gold);
    white-space: nowrap;
  }
  .copy {
    position: absolute;
    left: 104px;
    font-family: "Poiret One", sans-serif;
    font-size: 22px;
    line-height: 27px;
    color: var(--white);
    white-space: nowrap;
  }
  .copy--intro { top: 153px; }
  .copy--highlights { top: 274px; left: 102px; }
  .copy--extras { top: 355px; left: 102px; }

  .price-note {
    position: absolute;
    left: 880px; top: 70px;
    width: 240px;
    font-family: "Poiret One", sans-serif;
    font-size: 20px;
    line-height: 24px;
    color: var(--gold);
    text-align: right;
    transform: rotate(22deg);
    transform-origin: center;
    white-space: nowrap;
  }

  .contact {
    position: absolute;
    top: 466px;
    font-family: "Poiret One", sans-serif;
    font-size: 16px;
    line-height: 19px;
    color: var(--white);
    font-style: normal;
    white-space: nowrap;
  }
  .contact--address { left: 262px; }
  .contact--reach { left: 408px; }

  .mood-photo {
    position: absolute;
    left: 794px; top: 292px;
    width: 339px; height: 226px;
    border: 3px solid var(--gold);
    background:
      radial-gradient(ellipse at 68% 45%, var(--photo-warm) 0%, rgba(215,154,62,0.4) 35%, rgba(58,42,30,0) 70%),
      linear-gradient(180deg, #2a1f18 0%, var(--photo-dark) 70%, #4a3a30 100%);
  }
</style>
</head>
<body>
<main class="canvas">

  <section class="card card--front">
    <div class="emblem-area" role="img" aria-label="Goldenes Herz aus Messer und Gabel mit Funkeln"></div>
    <h1 class="event-title">Küchenparty</h1>
    <div class="brand">Kaltwinds am See</div>
  </section>

  <section class="card card--back">
    <h2 class="headline">Den Valentinstag mal anders beginnen</h2>

    <p class="copy copy--intro">mit höchstem Genuss aus Küche und Keller<br>bei der Küchenparty im Kaltwds am See.</p>
    <p class="copy copy--highlights">Für Sie individuell angerichtete Speise<br>die Küche in action für Sie!</p>
    <p class="copy copy--extras">Weine der Region – DJ und Party</p>

    <p class="price-note">Preis 98,00 €<br>inklusive: Aperitif<br>Grosse Speisenvarietät<br>(5 Gänge plus)<br>Regionale und<br>italienische Weine</p>

    <div class="brand">Kaltwinds am See</div>
    <address class="contact contact--address">Kaltwinds am See<br>Lore-Fink platz 7<br>71032 Böblingen</address>
    <address class="contact contact--reach">Tel: 07031 58 317 6<br>Mail: event@kaltwinds-beispiel.de<br>www.kaltwinds-beispiel.de</address>

    <div class="mood-photo" role="img" aria-label="Foto: Rotweinflasche und Glas mit Teelichtern vor warmem Herz-Lichterglanz"></div>
  </section>

</main>
</body>
</html>
```